Piano genealogy graphs template, for a large poster printing

Hello and thank you for your interest in my project.
I need a poster template, so I can create structures similar to the one I have uploaded. I want to completely replace or improve my poor previous design which is attached.
I need to be able to input names and dates into boxes of various colors, arrows pointing between boxes. I would also like to be able to label each graph (not each box).
I am looking at something that would be legible when printed, in a one consistent professional layout of 2A0 (around 1189x1682 mm) poster (I know it is large). The design template required here can include just few sample text boxes with sample flags on a suitable background, for me to multiply later and spread across the whole poster.
The positioning of the boxes is not important.
Please let me know if more clarification is required.
Thank you for your help.

Feel free to follow what I have attached in the file, or change the design completely.

UPDATE 4/12: I have uploaded two more graphs as an example. At this stage of the contest, I would like to have one of those graphs done, and I am planning to offer a 'freelance job' to one or two designers, who will be willing to do the whole 10 graphs on one poster.

Reason: Dear Designers, Since the project is rather complex and large-scale, I have decided to give everyone more time to work on their designs. I will consider extending it further if any of you require additional time. Best wishes, leopold

Dear Designers, I would like to inform you that the contest for my poster is now closed and that I have assigned the prizes. I would like to thank all of you for submiting your high-quality designs, and for your participation. It was a great pleasure working with all of you. Due to the large size of the project itself (large number of graphs to be fitted on a single poster), I had to focus on providing feedback to only those designers who provided projects closest to what I was expecting at the early stages of the contest. I wish you all the best for the future, Kind regards, Leopold

Target Market(s)

Pianists, historians

Industry/Entity Type

Printing

Requirements
Must have
• Consistent design, but allow to clearly delineate various genealogy trees.

```html
<!DOCTYPE html>
<html lang="en">
<head>
<meta charset="utf-8">
<title>Genealogical Trees of Pianists</title>
<link href="https://fonts.googleapis.com/css2?family=Nunito+Sans:wght@600;700&family=Source+Sans+3:wght@400;600;700&display=swap" rel="stylesheet">
<style>
  :root{
    --page:#e6e4e0;
    --navy-top:#073349;
    --navy-bottom:#021a2b;
    --title:#22c7b4;
    --head:#1cc3c4;
    --head-dark:#12aeb4;
    --body:#4ccd6c;
    --edge:#a6f2cf;
    --ink:#0b2a33;
    --ink-soft:#174a3a;
    --link:#2fb6e0;
    --flag-blue:#1c3fbf;
    --flag-white:#ffffff;
    --flag-red:#e0262c;
  }
  *{box-sizing:border-box;margin:0;padding:0}
  html,body{width:1200px;height:1148px;overflow:hidden;background:var(--page)}
  .poster{
    position:absolute;left:210px;top:24px;width:780px;height:1100px;
    background:linear-gradient(160deg,var(--navy-top) 0%,var(--navy-bottom) 70%);
    font-family:"Source Sans 3",sans-serif;overflow:hidden;
  }
  .poster-title{
    position:absolute;top:62px;width:100%;text-align:center;
    font-family:"Nunito Sans",sans-serif;font-weight:700;font-size:25px;color:var(--title);
  }
  .links{position:absolute;inset:0}
  .links path{fill:none;stroke:var(--link);stroke-width:2;stroke-dasharray:4 3}
  .card{
    position:absolute;border:2px solid var(--edge);border-radius:10px;overflow:hidden;
    background:var(--body);box-shadow:0 3px 8px rgba(0,0,0,.35);
  }
  .card-head{
    display:flex;align-items:center;gap:8px;padding:5px 10px;
    background:linear-gradient(180deg,var(--head),var(--head-dark));
  }
  .card-head h3{
    flex:1;text-align:center;font-size:9.5px;line-height:1.15;font-weight:700;color:var(--ink);
  }
  .card-solo{display:flex;align-items:center;gap:8px;padding:6px 12px}
  .card-solo h3{flex:1;text-align:center;font-size:10px;line-height:1.2;font-weight:700;color:var(--ink)}
  .students{list-style:none;padding:8px 10px 6px}
  .students li{
    display:flex;justify-content:space-between;align-items:center;
    font-size:8.5px;line-height:11px;color:var(--ink-soft);
  }
  .flag{
    flex:none;width:14px;height:9px;border:1px solid var(--flag-white);
    background:linear-gradient(90deg,var(--flag-blue) 33%,var(--flag-white) 33% 66%,var(--flag-red) 66%);
  }
</style>
</head>
<body>
<main class="poster">
  <h1 class="poster-title">Genealogical Trees of Pianists</h1>

  <svg class="links" width="780" height="1100" viewBox="0 0 780 1100" aria-hidden="true">
    <defs>
      <marker id="arrow" viewBox="0 0 8 8" refX="4" refY="4" markerWidth="6" markerHeight="6" orient="auto">
        <path d="M0 0 L8 4 L0 8 Z" fill="#2fb6e0" stroke="none" style="stroke-dasharray:none"/>
      </marker>
    </defs>
    <path d="M402 965 V925" marker-end="url(#arrow)"/>
    <path d="M402 875 V840 H230 V794" marker-end="url(#arrow)"/>
    <path d="M402 840 H417 V804" marker-end="url(#arrow)"/>
    <path d="M402 840 H607 V779" marker-end="url(#arrow)"/>
    <path d="M310 740 H200 V694" marker-end="url(#arrow)"/>
    <path d="M525 720 H615 V684" marker-end="url(#arrow)"/>
    <path d="M415 635 V594" marker-end="url(#arrow)"/>
    <path d="M300 565 H190 V559" marker-end="url(#arrow)"/>
    <path d="M515 490 H600 V469" marker-end="url(#arrow)"/>
    <path d="M370 430 V352 H160 V334" marker-end="url(#arrow)"/>
    <path d="M370 352 H317 V286" marker-end="url(#arrow)"/>
    <path d="M370 352 H455 V334" marker-end="url(#arrow)"/>
    <path d="M455 352 H610 V329" marker-end="url(#arrow)"/>
    <path d="M317 240 V215 H150 V199" marker-end="url(#arrow)"/>
    <path d="M317 215 V199" marker-end="url(#arrow)"/>
    <path d="M455 245 V215 H452 V199" marker-end="url(#arrow)"/>
    <path d="M610 240 V199" marker-end="url(#arrow)"/>
  </svg>

  <!-- Row 1 -->
  <section class="card" style="left:55px;top:110px;width:145px">
    <header class="card-head"><span class="flag"></span><h3>Henri Valmont<br>(1916-2008) Students:</h3></header>
    <ul class="students"><li>Jean-Luc Marchand (1947)<span class="flag"></span></li><li>Jacques Fournel (1947)<span class="flag"></span></li><li>Jean-Marc Delorme (1944)<span class="flag"></span></li></ul>
  </section>
  <section class="card" style="left:220px;top:110px;width:145px">
    <header class="card-head"><span class="flag"></span><h3>Henri Valmont<br>(1916-2008) Students:</h3></header>
    <ul class="students"><li>Jean-Luc Marchand (1947)<span class="flag"></span></li><li>Jacques Fournel (1947)<span class="flag"></span></li><li>Jean-Marc Delorme (1944)<span class="flag"></span></li></ul>
  </section>
  <section class="card" style="left:380px;top:110px;width:145px">
    <header class="card-head"><span class="flag"></span><h3>Henri Valmont<br>(1916-2008) Students:</h3></header>
    <ul class="students"><li>Jean-Luc Marchand (1947)<span class="flag"></span></li><li>Jacques Fournel (1947)<span class="flag"></span></li><li>Jean-Marc Delorme (1944)<span class="flag"></span></li></ul>
  </section>
  <section class="card" style="left:540px;top:110px;width:145px">
    <header class="card-head"><span class="flag"></span><h3>Henri Valmont<br>(1916-2008) Students:</h3></header>
    <ul class="students"><li>Jean-Luc Marchand (1947)<span class="flag"></span></li><li>Jacques Fournel (1947)<span class="flag"></span></li><li>Jean-Marc Delorme (1944)<span class="flag"></span></li></ul>
  </section>

  <!-- Row 2 -->
  <section class="card" style="left:75px;top:240px;width:170px">
    <header class="card-head"><span class="flag"></span><h3>Henri Valmont<br>(1916-2008) Students:</h3></header>
    <ul class="students"><li>Jean-Luc Marchand (1947)<span class="flag"></span></li><li>Jacques Fournel (1947)<span class="flag"></span></li><li>Jean-Marc Delorme (1944)<span class="flag"></span></li></ul>
  </section>
  <section class="card card-solo" style="left:265px;top:240px;width:105px">
    <span class="flag"></span><h3>Henri Valmont<br>(1916-2008)</h3>
  </section>
  <section class="card" style="left:382px;top:245px;width:145px">
    <header class="card-head"><span class="flag"></span><h3>Henri Valmont<br>(1916-2008) Students:</h3></header>
    <ul class="students"><li>Jean-Luc Marchand (1947)<span class="flag"></span></li><li>Jacques Fournel (1947)<span class="flag"></span></li><li>Jean-Marc Delorme (1944)<span class="flag"></span></li></ul>
  </section>
  <section class="card" style="left:540px;top:240px;width:145px">
    <header class="card-head"><span class="flag"></span><h3>Henri Valmont<br>(1916-2008) Students:</h3></header>
    <ul class="students"><li>Jean-Luc Marchand (1947)<span class="flag"></span></li><li>Jacques Fournel (1947)<span class="flag"></span></li><li>Jean-Marc Delorme (1944)<span class="flag"></span></li></ul>
  </section>

  <!-- Row 3 -->
  <section class="card" style="left:100px;top:395px;width:185px">
    <header class="card-head"><span class="flag"></span><h3>Henri Valmont<br>(1916-2008) Students:</h3></header>
    <ul class="students">
      <li>Jean-Luc Marchand (1947)<span class="flag"></span></li><li>Jacques Fournel (1947)<span class="flag"></span></li><li>Jean-Marc Delorme (1944)<span class="flag"></span></li>
      <li>Jean-Luc Marchand (1947)<span class="flag"></span></li><li>Jacques Fournel (1947)<span class="flag"></span></li><li>Jean-Marc Delorme (1944)<span class="flag"></span></li>
      <li>Jean-Luc Marchand (1947)<span class="flag"></span></li><li>Jacques Fournel (1947)<span class="flag"></span></li><li>Jean-Marc Delorme (1944)<span class="flag"></span></li>
    </ul>
  </section>
  <section class="card" style="left:300px;top:430px;width:215px">
    <header class="card-head"><span class="flag"></span><h3>Henri Valmont<br>(1916-2008) Students:</h3></header>
    <ul class="students">
      <li>Jean-Luc Marchand (1947)<span class="flag"></span></li><li>Jacques Fournel (1947)<span class="flag"></span></li><li>Jean-Marc Delorme (1944)<span class="flag"></span></li>
      <li>Jean-Luc Marchand (1947)<span class="flag"></span></li><li>Jacques Fournel (1947)<span class="flag"></span></li><li>Jean-Marc Delorme (1944)<span class="flag"></span></li>
      <li>Jean-Luc Marchand (1947)<span class="flag"></span></li><li>Jacques Fournel (1947)<span class="flag"></span></li><li>Jean-Marc Delorme (1944)<span class="flag"></span></li>
    </ul>
  </section>
  <section class="card" style="left:525px;top:385px;width:165px">
    <header class="card-head"><span class="flag"></span><h3>Henri Valmont<br>(1916-2008) Students:</h3></header>
    <ul class="students"><li>Jean-Luc Marchand (1947)<span class="flag"></span></li><li>Jacques Fournel (1947)<span class="flag"></span></li><li>Jean-Marc Delorme (1944)<span class="flag"></span></li></ul>
  </section>

  <!-- Row 4 -->
  <section class="card" style="left:125px;top:600px;width:165px">
    <header class="card-head"><span class="flag"></span><h3>Henri Valmont<br>(1916-2008) Students:</h3></header>
    <ul class="students"><li>Jean-Luc Marchand (1947)<span class="flag"></span></li><li>Jacques Fournel (1947)<span class="flag"></span></li><li>Jean-Marc Delorme (1944)<span class="flag"></span></li></ul>
  </section>
  <section class="card" style="left:310px;top:635px;width:215px">
    <header class="card-head"><span class="flag"></span><h3>Henri Valmont<br>(1916-2008) Students:</h3></header>
    <ul class="students">
      <li>Jean-Luc Marchand (1947)<span class="flag"></span></li><li>Jacques Fournel (1947)<span class="flag"></span></li><li>Jean-Marc Delorme (1944)<span class="flag"></span></li>
      <li>Jean-Luc Marchand (1947)<span class="flag"></span></li><li>Jacques Fournel (1947)<span class="flag"></span></li><li>Jean-Marc Delorme (1944)<span class="flag"></span></li>
      <li>Jean-Luc Marchand (1947)<span class="flag"></span></li><li>Jacques Fournel (1947)<span class="flag"></span></li><li>Jean-Marc Delorme (1944)<span class="flag"></span></li>
    </ul>
  </section>
  <section class="card" style="left:540px;top:595px;width:150px">
    <header class="card-head"><span class="flag"></span><h3>Henri Valmont<br>(1916-2008) Students:</h3></header>
    <ul class="students"><li>Jean-Luc Marchand (1947)<span class="flag"></span></li><li>Jacques Fournel (1947)<span class="flag"></span></li><li>Jean-Marc Delorme (1944)<span class="flag"></span></li></ul>
  </section>

  <!-- Row 5 -->
  <section class="card card-solo" style="left:160px;top:746px;width:140px">
    <span class="flag"></span><h3>Henri Valmont<br>(1916-2008)</h3>
  </section>
  <section class="card card-solo" style="left:540px;top:731px;width:135px">
    <span class="flag"></span><h3>Henri Valmont<br>(1916-2008)</h3>
  </section>

  <!-- Roots -->
  <section class="card card-solo" style="left:335px;top:875px;width:135px">
    <span class="flag"></span><h3>Henri Valmont<br>(1916-2008)</h3>
  </section>
  <section class="card card-solo" style="left:335px;top:965px;width:135px">
    <span class="flag"></span><h3>Henri Valmont<br>(1916-2008)</h3>
  </section>
</main>
</body>
</html>
```